Vielen Dank für die tolle und unkomplizierte Zusammenarbeit.
Zielgruppe
Wir informieren, trainieren und coachen Eltern darin, wie sie ihre Babies und Kleinkinder zum Schlafen brinen.
Zielgruppe sind alle Eltern, in der Regel Akademiker, deren 0-3 jährigen Kinder Ein- und/oder Durchschlafprobleme haben
Aufgabenstellung
Ich bräuchte bitte Vorschläge mit 2 verschiedenen Namen, da ich in diesem Jahr heiraten werde:
- mein aktueller Name ist Wiebke Raschdorf
- mein künftiger Name ist Wiebke Ostner
- Eventuell kann das CD meine Initialien im Firmennamen beinhalten, wie z.B.: WOlkenreise ruhecoaching (nur eine Idee, auf die ich allerdings nicht festgelegt bin :-)) Ihr wisst das besser
- ich bräuchte bitte auch einen Header für meine bereits existierende Webkasten Domain
- das CD sollte nicht zu verspielt sein und kompetent wirken

```html
<!DOCTYPE html>
<html lang="de">
<head>
<meta charset="utf-8">
<title>Wolkenreise Ruhecoaching – Geschäftsausstattung</title>
<link href="https://fonts.googleapis.com/css2?family=Ubuntu:wght@400;500;700&family=Arimo:wght@400;700&display=swap" rel="stylesheet">
<style>
  :root {
    --stage: #d8d2ca;
    --paper: #ffffff;
    --sky: #cfe6f5;
    --slate: #5a5b5e;
    --ink: #4f5358;
    --text: #8c8f93;
    --accent: #2f8fbf;
  }
  * { margin: 0; padding: 0; box-sizing: border-box; }
  html, body {
    width: 1200px; height: 1189px; overflow: hidden;
    background: var(--stage);
    font-family: "Arimo", Arial, sans-serif;
  }
  .stage { position: relative; width: 1200px; height: 1189px; }

  .brand {
    position: absolute;
    display: flex; align-items: center; gap: 8px;
    font-family: "Ubuntu", sans-serif; font-weight: 500;
    color: var(--ink); line-height: 1.05;
  }
  .brand-dot { border-radius: 50%; background: var(--accent); flex: none; }

  /* Letterhead */
  .letterhead {
    position: absolute; left: 58px; top: 157px; width: 644px; height: 911px;
    background: var(--paper); box-shadow: 0 4px 14px rgba(0,0,0,.25); overflow: hidden;
  }
  .top-band { position: absolute; left: 0; top: 0; width: 100%; height: 11px; background: var(--sky); }
  .letterhead .brand { right: 46px; top: 50px; font-size: 27px; text-align: left; }
  .letterhead .brand-dot { width: 14px; height: 14px; }
  .sender-line { position: absolute; left: 52px; top: 186px; font-size: 6px; color: var(--text); }
  .recipient { position: absolute; left: 52px; top: 208px; font-size: 9px; line-height: 12px; color: var(--text); }
  .subject { position: absolute; left: 52px; top: 267px; font-size: 9px; color: var(--text); }
  .letter-body {
    position: absolute; left: 52px; top: 300px; width: 418px;
    font-size: 9.6px; line-height: 10px; color: var(--text);
  }
  .letter-body .salutation { margin-bottom: 14px; }
  .closing { position: absolute; left: 52px; top: 680px; font-size: 8.4px; color: var(--text); }
  .signature { position: absolute; left: 52px; top: 706px; font-size: 8.4px; line-height: 10px; color: var(--text); }
  .footer {
    position: absolute; left: 0; bottom: 0; width: 100%; height: 50px;
    background: var(--slate); border-top: 3px solid var(--paper);
  }
  .footer-rule { position: absolute; left: 0; bottom: 50px; width: 100%; height: 1px; background: var(--slate); }
  .footer-col {
    position: absolute; top: 8px; font-size: 5.6px; line-height: 7px;
    color: #fff; font-weight: 700;
  }

  /* Business cards */
  .card {
    position: absolute; left: 742px; width: 373px; background: var(--paper);
    box-shadow: 0 4px 12px rgba(0,0,0,.25); overflow: hidden;
  }
  .card-front { top: 309px; height: 241px; }
  .card-back { top: 641px; height: 239px; }
  .card-front .brand { left: 37px; top: 36px; font-size: 22px; }
  .card-front .brand-dot { width: 11px; height: 11px; }
  .card-back .brand { left: 65px; top: 96px; font-size: 30px; }
  .card-back .brand-dot { width: 15px; height: 15px; }
  .card-panel {
    position: absolute; left: 0; bottom: 0; width: 100%; height: 116px;
    background: var(--slate); color: #fff; font-family: "Ubuntu", sans-serif;
  }
  .card-name { position: absolute; left: 40px; top: 20px; font-size: 14px; font-weight: 500; }
  .card-role { position: absolute; left: 40px; top: 38px; font-size: 7px; font-weight: 700; }
  .card-address { position: absolute; left: 40px; top: 64px; font-size: 9.5px; line-height: 12px; font-weight: 500; }
  .card-phone { position: absolute; left: 184px; top: 24px; font-size: 9.5px; line-height: 12px; font-weight: 500; }
  .card-web { position: absolute; left: 184px; top: 62px; font-size: 9.5px; line-height: 12px; font-weight: 500; }
</style>
</head>
<body>
<main class="stage">

  <article class="letterhead">
    <div class="top-band"></div>
    <div class="brand"><span class="brand-dot"></span><span>Wolkenreise<br>Ruhecoaching</span></div>

    <p class="sender-line">Wiebke Ostner Lindenweg 44 12345 Wolkenstadt</p>
    <p class="recipient">Sternenhof GmbH<br>Firmenstraße 12<br>12345 Firmenort</p>
    <p class="subject">Betreffzeile</p>

    <div class="letter-body">
      <p class="salutation">Sehr geehrte Damen und Herren,</p>
      <p>Lorem ipsum dolor sit amet, consetetur sadipscing elitr, sed diam nonumy eirmod tempor invidunt ut labore et dolore magna aliquyam erat, sed diam voluptua. At vero eos et accusam et justo duo dolores et ea rebum. Stet clita kasd gubergren, no sea takimata sanctus est Lorem ipsum dolor sit amet. Lorem ipsum dolor sit amet, consetetur sadipscing elitr, sed diam nonumy eirmod tempor invidunt ut labore et dolore magna aliquyam erat, sed diam voluptua. At vero eos et accusam et justo duo dolores et ea rebum. Stet clita kasd gubergren, no sea takimata sanctus est Lorem ipsum dolor sit amet. Lorem ipsum dolor sit amet, consetetur sadipscing elitr, sed diam nonumy eirmod tempor invidunt ut labore et dolore magna aliquyam erat, sed diam voluptua. At vero eos et accusam et justo duo dolores et ea rebum. Stet clita kasd gubergren, no sea takimata sanctus est Lorem ipsum dolor sit amet.</p>
      <p>Duis autem vel eum iriure dolor in hendrerit in vulputate velit esse molestie consequat, vel illum dolore eu feugiat nulla facilisis at vero eros et accumsan et iusto odio dignissim qui blandit praesent luptatum zzril delenit augue duis dolore te feugait nulla facilisi. Lorem ipsum dolor sit amet, consectetuer adipiscing elit, sed diam nonummy nibh euismod tincidunt ut laoreet dolore magna aliquam erat volutpat.</p>
      <p>Ut wisi enim ad minim veniam, quis nostrud exerci tation ullamcorper suscipit lobortis nisl ut aliquip ex ea commodo consequat. Duis autem vel eum iriure dolor in hendrerit in vulputate velit esse molestie consequat, vel illum dolore eu feugiat nulla facilisis at vero eros et accumsan et iusto odio dignissim qui blandit praesent luptatum zzril delenit augue duis dolore te feugait nulla facilisi.</p>
      <p>At vero eos et accusam et justo duo dolores et ea rebum. Stet clita kasd gubergren, no sea takimata sanctus est Lorem ipsum dolor sit amet. Lorem ipsum dolor sit amet, consetetur sadipscing elitr, sed diam nonumy eirmod tempor invidunt ut labore et dolore magna aliquyam erat, sed diam voluptua. At vero eos et accusam et justo duo dolores et ea rebum. Stet clita kasd gubergren, no sea takimata sanctus est Lorem ipsum dolor sit amet. At accusam aliquyam diam diam dolore dolores duo eirmod eos erat, et nonumy sed tempor et et invidunt justo labore. Lorem ipsum dolor sit amet, consetetur</p>
    </div>

    <p class="closing">Mit freundlichen Grüßen</p>
    <p class="signature">Wiebke Ostner<br>Beispielort, 31. Juli 2014</p>

    <div class="footer-rule"></div>
    <footer class="footer">
      <p class="footer-col" style="left:52px">Wiebke Ostner<br>Lindenweg 44<br>D-12345 Wolkenstadt</p>
      <p class="footer-col" style="left:186px">Inhaberin<br>Wiebke Ostner</p>
      <p class="footer-col" style="left:314px">Tel. 01234 / 5678<br>Fax 01234 / 5679<br>info@wolkenreise.de<br>www.wolkenreise.de</p>
      <p class="footer-col" style="left:441px">Bank Wolkenstadt<br>IBAN DE00 0000 0000 0000 00<br>BIC WOLKDEXX</p>
    </footer>
  </article>

  <section class="card card-front">
    <div class="top-band"></div>
    <div class="brand"><span class="brand-dot"></span><span>Wolkenreise<br>Ruhecoaching</span></div>
    <div class="card-panel">
      <p class="card-name">Wiebke Ostner</p>
      <p class="card-role">Berufsbezeichnung</p>
      <p class="card-address">Lindenweg 44<br>D-12345 Wolkenstadt</p>
      <p class="card-phone">Tel.04711-2580<br>Fax.04711-2581</p>
      <p class="card-web">info@wolkenreise.de<br>www.wolkenreise.de</p>
    </div>
  </section>

  <section class="card card-back">
    <div class="brand"><span class="brand-dot"></span><span>Wolkenreise<br>Ruhecoaching</span></div>
  </section>

</main>
</body>
</html>
```